Bramwell Exteriors Needs a New Website!

We are an exteriors company specializing in vinyl siding, Kestrel Fibre siding, aluminum soffit/fascia, trough. We do new construction work as well as renovations. We also build detached garages.
You can view our current website at www.bramwellbuilders.ca
I want to completely overhaul the website.
Our services are different now as we no longer do new home construction as well as we do not do the snow clearing.
I want to focus on 2 things in particular on the website:

1/ Exterior renovations

2/ Detached Garage construction.

I have included our logo in the attached files to use as well.

Some features we would like:

1/ Be able to easily attach a video from Youtube/Vimeo to highlight a product or service
2/ Quick chat or contact button that we can talk to a potential client quickly
3/ Meet the Team page that is interesting and fresh
4/ Place for us to put in helpful exterior tips/suggestions for homeowners.

Content is not important, but looking for the best design that will attract people once they click on our page and want to renovate with us.

Target Market(s)

People looking for renovations on their home, people looking to build a detached garage.

Industry/Entity Type

Residential Construction

Coding

Coded - Design and coding required

Number of Pages Required

5+ page

Font styles to use
Sans Serif

Requirements
Must have
• Fresh and exciting home page.

Simple design. Don't want it over complicated or too much information to confuse the potential client.

Easy way to contact us.

Meet the team page that instills confidence
Nice to have
• Colour of website to go off our logo. Doesn't need to be an exact match, but something that goes well with our blue and grey.

```html
<!DOCTYPE html>
<html lang="en">
<head>
<meta charset="utf-8">
<title>Bramwell Exteriors</title>
<link href="https://fonts.googleapis.com/css2?family=Arimo:wght@400;700&family=Open+Sans:wght@400;600;700&display=swap" rel="stylesheet">
<style>
:root{
  --blue:#1a6fb8;
  --blue-dark:#0f4f8a;
  --ink:#222;
  --text:#555;
  --grey:#f3f3f3;
  --line:#d6d6d6;
  --footer:#0d1420;
  --white:#fff;
}
*{box-sizing:border-box;margin:0;padding:0}
html,body{width:1200px;height:4573px;overflow:hidden}
body{position:relative;font-family:"Open Sans",sans-serif;color:var(--ink);background:var(--white)}
.abs{position:absolute}
.section-title{position:absolute;left:0;width:1200px;text-align:center;color:var(--blue);font-family:"Arimo",sans-serif;font-weight:700;font-size:31px;letter-spacing:.5px}
.btn{display:inline-block;border-radius:20px;font-family:"Open Sans",sans-serif;font-size:14px;text-align:center;white-space:nowrap}
.btn-outline{border:1.5px solid #444;color:#333;background:var(--white)}
.btn-solid{background:var(--blue);color:var(--white);font-weight:700}

/* top bar */
.topbar{top:0;left:0;width:1200px;height:36px;background:var(--blue);color:var(--white);font-size:13px}
.topbar span{position:absolute;top:9px;white-space:nowrap}
.topbar svg{vertical-align:-2px;margin-right:7px}
.social{position:absolute;top:8px;width:20px;height:20px;border-radius:50%;background:rgba(255,255,255,.25)}

/* header */
.header{top:36px;left:0;width:1200px;height:81px;background:var(--white)}
.brand{position:absolute;left:142px;top:20px;display:flex;align-items:center;gap:9px}
.brand-dot{width:40px;height:40px;border-radius:50%;background:var(--blue);flex:none}
.brand-name{font-family:"Open Sans",sans-serif;font-weight:700;font-size:18px;color:var(--blue);letter-spacing:.3px;white-space:nowrap}
.nav{position:absolute;top:34px;left:461px;display:flex;gap:23px;font-size:13.5px;color:#444;white-space:nowrap}
.nav .active{color:var(--blue);font-weight:600;border-bottom:2px solid var(--blue);padding-bottom:4px}
.quote{position:absolute;left:905px;top:26px;width:154px;height:34px;line-height:31px;border:1.5px solid var(--blue);color:var(--blue);font-size:13.5px;border-radius:20px;text-align:center}

/* hero */
.hero{top:117px;left:0;width:1200px;height:563px;background:linear-gradient(90deg,#3b2a22 0%,#7a4f3a 35%,#8e6a55 55%,#5d6b4e 85%,#3e4a33 100%)}
.hero-shade{top:117px;left:0;width:1200px;height:563px;background:linear-gradient(90deg,rgba(0,0,0,.45),rgba(0,0,0,.05) 60%)}
.hero-kicker{left:145px;top:324px;color:var(--white);font-family:"Arimo",sans-serif;font-weight:700;font-size:19px;white-space:nowrap}
.hero-title{left:143px;top:366px;color:var(--white);font-family:"Arimo",sans-serif;font-weight:700;font-size:34px;line-height:46px;white-space:nowrap}
.scroll-down{left:570px;top:652px;width:60px;height:60px;border-radius:50%;background:var(--white)}

/* renovations */
.card{position:absolute;top:857px;width:218px;height:217px;border-radius:8px}
.card-label{position:absolute;top:1092px;width:218px;text-align:center;font-family:"Arimo",sans-serif;font-weight:700;font-size:16.5px;line-height:23px;color:#333}
.card-btn{position:absolute;top:1160px;height:32px;line-height:29px;width:108px}

/* about */
.about{top:1297px;left:0;width:1200px;height:660px;background:var(--grey)}
.about-title{left:622px;top:1400px;font-family:"Arimo",sans-serif;font-weight:700;font-size:31px;color:var(--blue)}
.about-lead{left:622px;top:1456px;width:440px;font-weight:700;font-size:16.5px;line-height:27px;color:#333;letter-spacing:.3px}
.about-body{left:622px;top:1553px;width:440px;font-size:13.5px;line-height:25.5px;color:var(--text)}
.about-cta{left:621px;top:1783px;display:flex;align-items:center;gap:14px;font-size:15px;color:#333;white-space:nowrap}

/* garage band */
.garage{top:1900px;left:0;width:1200px;height:460px;background:linear-gradient(180deg,#2f3a44 0%,#4a4036 55%,#2b2f2f 100%)}
.garage-title{left:0;top:2060px;width:1200px;text-align:center;color:var(--white);font-family:"Arimo",sans-serif;font-weight:700;font-size:30px}
.garage-text{left:150px;top:2108px;width:900px;text-align:center;color:var(--white);font-weight:700;font-size:15px;line-height:23px}
.garage-btn{left:518px;top:2171px;width:164px;height:34px;line-height:34px;letter-spacing:1px}

/* why choose */
.why-label{position:absolute;font-size:16.5px;color:#222;white-space:nowrap}
.why-icon{position:absolute;width:96px;height:96px;border-radius:50%;background:var(--white);border:7px solid #e9e9e9;box-shadow:0 2px 6px rgba(0,0,0,.12)}
.why-icon svg{position:absolute;left:20px;top:20px}
.why-icon.active{background:var(--blue);border-color:#e9e9e9}
.why-note{left:801px;top:2930px;width:260px;font-size:13.5px;line-height:21px;color:#555}

/* helpful band */
.helpful{top:3050px;left:0;width:1200px;height:470px;background:linear-gradient(180deg,#1a6fb8 0%,#24557f 45%,#173a55 100%)}
.helpful-title{left:0;top:3222px;width:1200px;text-align:center;color:var(--white);font-family:"Arimo",sans-serif;font-weight:700;font-size:29px;line-height:38px}
.helpful-btn{left:508px;top:3317px;width:184px;height:36px;line-height:36px;background:var(--white);color:#222;font-weight:700}

/* reviews */
.review-lead{left:0;top:3695px;width:1200px;text-align:center;font-size:16px;color:#333}
.review-body{left:140px;top:3735px;width:920px;text-align:center;font-size:13.5px;line-height:21px;color:#333}
.review-name{left:0;top:3815px;width:1200px;text-align:center;font-weight:700;font-size:14px}
.dots{left:566px;top:3863px;display:flex;gap:7px}
.dots i{display:block;width:11px;height:11px;border-radius:50%;border:1.5px solid #999}
.dots i.on{background:#999}

/* footer */
.footer{top:3981px;left:0;width:1200px;height:542px;background:linear-gradient(180deg,#151b26 0%,#0b1019 60%,#101828 100%)}
.footer-title{position:absolute;color:var(--white);font-family:"Arimo",sans-serif;font-weight:700;font-size:23px}
.field{position:absolute;height:33px;background:var(--white);border-radius:3px;font-size:12.5px;color:#444;padding:8px 10px}
.submit{left:142px;top:4316px;width:112px;height:32px;line-height:32px;font-size:16px}
.contact-row{position:absolute;left:797px;display:flex;gap:14px;color:var(--white);font-size:13.5px;line-height:21px;white-space:nowrap}
.contact-row .ico{flex:none;width:34px;height:34px;border-radius:50%;background:var(--white);display:flex;align-items:center;justify-content:center}
.contact-row b{font-weight:700}
.footer-link{position:absolute;top:4451px;font-size:14px;color:#ddd;white-space:nowrap}
.footer-link.active{color:var(--white);font-weight:700}
.footer-brand{left:796px;top:4436px;display:flex;align-items:center;gap:9px}
.copyright{top:4523px;left:0;width:1200px;height:50px;background:var(--blue);color:var(--white);text-align:center;line-height:50px;font-size:14.5px}
.chat{left:982px;top:3944px;width:80px;height:80px;border-radius:50%;background:var(--blue);color:var(--white);text-align:center;font-size:10px;padding-top:48px}
</style>
</head>
<body>

<div class="abs topbar">
  <span style="left:143px"><svg width="12" height="12" viewBox="0 0 24 24"><path fill="#fff" d="M6.6 10.8a15 15 0 0 0 6.6 6.6l2.2-2.2c.3-.3.7-.4 1-.2 1.1.4 2.3.6 3.6.6.6 0 1 .4 1 1V20c0 .6-.4 1-1 1A17 17 0 0 1 3 4c0-.6.4-1 1-1h3.5c.6 0 1 .4 1 1 0 1.3.2 2.5.6 3.6.1.3 0 .7-.2 1z"/></svg>780-555-0148</span>
  <span style="left:291px"><svg width="14" height="11" viewBox="0 0 24 18"><path fill="#fff" d="M2 0h20a2 2 0 0 1 2 2v.5L12 10 0 2.5V2a2 2 0 0 1 2-2zm-2 5 12 7.5L24 5v11a2 2 0 0 1-2 2H2a2 2 0 0 1-2-2z"/></svg>info@bramwellbuilders.ca</span>
  <span style="left:849px">FOLLOW US:</span>
  <i class="social" style="left:956px"></i>
  <i class="social" style="left:995px"></i>
  <i class="social" style="left:1037px"></i>
</div>

<header class="abs header">
  <div class="brand"><i class="brand-dot"></i><span class="brand-name">BRAMWELL EXTERIORS</span></div>
  <nav class="nav">
    <span class="active">HOME</span><span>ABOUT</span><span>SERVICES</span><span>MEET THE TEAM</span><span>CONTACT</span>
  </nav>
  <div class="quote">REQUEST A QUOTE</div>
</header>

<div class="abs hero" role="img" aria-label="Photo of a family standing in front of a red brick home"></div>
<div class="abs hero-shade"></div>
<p class="abs hero-kicker">WE ARE AN EXTERIORS COMPANY SPECIALIZING IN</p>
<h1 class="abs hero-title">VINYL SIDING, KESTREL FIBRE<br>SIDING, ALUMINUM SOFFIT/<br>FASCIA, TROUGH.</h1>
<div class="abs scroll-down">
  <svg width="60" height="40" viewBox="0 0 60 40"><path d="M30 14v17M24 25l6 6 6-6" stroke="#333" stroke-width="2" fill="none"/></svg>
</div>

<h2 class="section-title" style="top:783px">EXTERIOR RENOVATIONS</h2>
<div class="card" style="left:142px;background:linear-gradient(160deg,#a7683f,#5c3520)" role="img" aria-label="Photo of a modern home with wood vinyl siding"></div>
<div class="card" style="left:374px;background:linear-gradient(160deg,#8b8a8a,#3d3a36)" role="img" aria-label="Photo of a house under siding installation"></div>
<div class="card" style="left:607px;background:linear-gradient(160deg,#6fa3d6,#d8dde2)" role="img" aria-label="Photo of a house with aluminum soffit and fascia"></div>
<div class="card" style="left:840px;background:linear-gradient(160deg,#8aa4c0,#6f8a3e)" role="img" aria-label="Photo of a timber frame with roof trough"></div>
<div class="card-label" style="left:142px">VINYL SIDING</div>
<div class="card-label" style="left:374px">KESTREL FIBRE<br>SIDING</div>
<div class="card-label" style="left:607px">ALUMINUM<br>SOFFIT/FASCIA</div>
<div class="card-label" style="left:840px">TROUGH</div>
<span class="btn btn-outline card-btn" style="left:197px">EXPLORE</span>
<span class="btn btn-solid card-btn" style="left:425px;border:1.5px solid var(--blue)">EXPLORE</span>
<span class="btn btn-outline card-btn" style="left:662px">EXPLORE</span>
<span class="btn btn-outline card-btn" style="left:895px">EXPLORE</span>

<section class="abs about"></section>
<svg class="abs" style="left:138px;top:1404px" width="444" height="444" viewBox="0 0 444 444">
  <circle cx="222" cy="222" r="219" fill="none" stroke="#9a9a9a" stroke-width="3"/>
  <path d="M222 441A219 219 0 0 1 3 222" fill="none" stroke="var(--blue)" stroke-width="5"/>
  <circle cx="222" cy="222" r="208" fill="#8a7b62"/>
</svg>
<div class="abs" style="left:152px;top:1418px;width:416px;height:416px;border-radius:50%;background:linear-gradient(150deg,#7d8f6a,#b09a78 55%,#6a604e)" role="img" aria-label="Video thumbnail of a worker installing siding on a house"></div>
<svg class="abs" style="left:329px;top:1596px" width="62" height="62" viewBox="0 0 62 62">
  <circle cx="31" cy="31" r="30" fill="#e01b1b"/><path d="M25 19l18 12-18 12z" fill="#fff"/>
</svg>
<h2 class="abs about-title">ABOUT US</h2>
<p class="abs about-lead">Honest and reliable construction service in Northfield and area. We take pride in each and every project.</p>
<p class="abs about-body">Lorem ipsum dolor sit amet, consectetuer adipiscing elit, sed diam nonummy nibh euismod tincidunt ut laoreet dolore magna werwe aliquam erat volutpat. Ut wisi enim ad minim veniam, quis nostrud exerci tation ullamcorper suscipit lobortis nisl ut aliquip ex eaererr commodo consequat. Duis autem vel eum iriure dolor in hendrerit in vulputate velit esse molestie consequat, vel illum dolore euwere feugiat nulla facilisis at vero eros et accumsan et iusto odiowererrr dignissim qui blandit praesent luptatum</p>
<div class="abs about-cta">
  <span class="btn btn-solid" style="width:120px;height:32px;line-height:32px;font-size:14.5px">READ MORE</span>
  <span>or</span>
  <span><svg width="15" height="15" viewBox="0 0 24 24" style="vertical-align:-2px;margin-right:4px"><path fill="var(--blue)" d="M6.6 10.8a15 15 0 0 0 6.6 6.6l2.2-2.2c.3-.3.7-.4 1-.2 1.1.4 2.3.6 3.6.6.6 0 1 .4 1 1V20c0 .6-.4 1-1 1A17 17 0 0 1 3 4c0-.6.4-1 1-1h3.5c.6 0 1 .4 1 1 0 1.3.2 2.5.6 3.6.1.3 0 .7-.2 1z"/></svg>CALL - 780-555-0148</span>
</div>

<div class="abs garage" role="img" aria-label="Photo of a detached garage and house at dusk"></div>
<div class="abs" style="top:1900px;left:0;width:1200px;height:460px;background:rgba(20,25,30,.35)"></div>
<svg class="abs" style="left:0;top:1895px" width="1200" height="470" viewBox="0 0 1200 470" preserveAspectRatio="none">
  <path d="M0 0H1200V20Q600 115 0 20Z" fill="var(--grey)"/>
  <path d="M0 458Q600 340 1200 458V470H0Z" fill="#fff"/>
</svg>
<h2 class="abs garage-title">DETACHED GARAGE CONSTRUCTION</h2>
<p class="abs garage-text">Lorem ipsum dolor sit amet, consectetuer adipiscing elit, sed diam nonummy nibh euismod tincidunt ut laoreet dolore magna ererere aliquam erat volutpat Quis nostrud exerci tation ullamcorper suscipit lobortis .</p>
<span class="abs btn btn-solid garage-btn">KNOW MORE</span>

<h2 class="section-title" style="top:2398px">WHY CHOOSE US?</h2>
<svg class="abs" style="left:0;top:2400px" width="1200" height="640" viewBox="0 0 1200 640">
  <g stroke="#dcdcdc" stroke-width="3">
    <line x1="456" y1="117" x2="600" y2="310"/><line x1="730" y1="117" x2="600" y2="310"/>
    <line x1="366" y1="310" x2="834" y2="310"/>
    <line x1="460" y1="504" x2="600" y2="310"/><line x1="733" y1="504" x2="600" y2="310"/>
  </g>
  <circle cx="600" cy="310" r="135" fill="#fff" stroke="#e5e5e5" stroke-width="6"/>
  <circle cx="600" cy="310" r="120" fill="#f6f6f6"/>
  <g fill="#ddd"><circle cx="515" cy="225" r="6"/><circle cx="685" cy="225" r="6"/><circle cx="472" cy="310" r="6"/><circle cx="728" cy="310" r="6"/><circle cx="515" cy="395" r="6"/><circle cx="685" cy="395" r="6"/></g>
  <circle cx="600" cy="268" r="34" fill="var(--blue)"/>
  <text x="600" y="350" text-anchor="middle" font-family="Open Sans, sans-serif" font-weight="700" font-size="22" fill="var(--blue)">BRAMWELL</text>
  <text x="600" y="374" text-anchor="middle" font-family="Open Sans, sans-serif" font-weight="700" font-size="13" fill="var(--blue)" letter-spacing="3">EXTERIORS</text>
</svg>

<div class="why-icon" style="left:408px;top:2469px"><svg width="42" height="42" viewBox="0 0 42 42" fill="none" stroke="var(--blue)" stroke-width="2"><path d="M21 4l13 5v10c0 9-6 15-13 18C14 34 8 28 8 19V9z"/><path d="M15 21l4 4 8-8"/></svg></div>
<div class="why-icon" style="left:682px;top:2469px"><svg width="42" height="42" viewBox="0 0 42 42" fill="none" stroke="var(--blue)" stroke-width="2"><circle cx="13" cy="26" r="5"/><circle cx="29" cy="26" r="5"/><path d="M4 40c0-5 4-8 9-8s9 3 9 8M20 40c0-5 4-8 9-8s9 3 9 8"/><rect x="15" y="3" width="22" height="13" rx="6"/></svg></div>
<div class="why-icon" style="left:318px;top:2662px"><svg width="42" height="42" viewBox="0 0 42 42" fill="none" stroke="var(--blue)" stroke-width="2"><path d="M6 14v14l10 8M36 14v14l-10 8"/><path d="M21 10l7 3v6c0 5-3 8-7 10-4-2-7-5-7-10v-6z"/></svg></div>
<div class="why-icon" style="left:779px;top:2662px"><svg width="42" height="42" viewBox="0 0 42 42" fill="none" stroke="var(--blue)" stroke-width="2"><path d="M5 20L21 6l16 14M9 17v19h24V17"/><path d="M21 16l2 4 4 .5-3 3 1 4-4-2-4 2 1-4-3-3 4-.5z"/></svg></div>
<div class="why-icon" style="left:412px;top:2856px"><svg width="42" height="42" viewBox="0 0 42 42" fill="none" stroke="var(--blue)" stroke-width="2"><rect x="6" y="6" width="26" height="32" rx="2"/><path d="M12 14h14M12 20h14M12 26h8"/><path d="M24 30l4 4 8-9"/></svg></div>
<div class="why-icon active" style="left:685px;top:2856px"><svg width="42" height="42" viewBox="0 0 42 42" fill="none" stroke="#fff" stroke-width="2"><circle cx="21" cy="16" r="11"/><path d="M24 11h-4a2.5 2.5 0 0 0 0 5h2a2.5 2.5 0 0 1 0 5h-4M21 8v3M21 21v3"/><path d="M4 34h8l6 3h10l10-6"/></svg></div>

<span class="why-label" style="left:250px;top:2504px">Unrivalled Quality</span>
<span class="why-label" style="left:791px;top:2504px">Superior Communication</span>
<span class="why-label" style="left:152px;top:2709px">Safety Conscience</span>
<span class="why-label" style="left:890px;top:2709px">Certified Experience</span>
<span class="why-label" style="left:203px;top:2902px">Guaranteed Satisfaction</span>
<span class="why-label" style="left:801px;top:2902px;color:var(--blue);font-weight:700">Competitive Pricing</span>
<p class="abs why-note">Although we offer the best in services, we won't blow your budget on the job. We also take credit cards in our renovations division.</p>

<div class="abs helpful" role="img" aria-label="Photo of a modern home with a pool at night"></div>
<svg class="abs" style="left:0;top:3045px" width="1200" height="480" viewBox="0 0 1200 480" preserveAspectRatio="none">
  <path d="M0 0H1200V15Q700 95 0 35Z" fill="#fff"/>
  <path d="M0 460Q550 330 1200 445V480H0Z" fill="#fff"/>
</svg>
<h2 class="abs helpful-title">HELPFUL<br>EXTERIOR SUGGESTIONS FOR HOMEOWNERS</h2>
<span class="abs btn helpful-btn">CONTACT US TODAY</span>

<h2 class="section-title" style="top:3553px">CUSTOMER REVIEWS</h2>
<svg class="abs" style="left:568px;top:3614px" width="64" height="64" viewBox="0 0 64 64">
  <circle cx="32" cy="32" r="31" fill="#e8e8e8"/>
  <path d="M20 24h9v9c0 6-3 10-8 11l-1-3c3-1 4-3 4-6h-4zM35 24h9v9c0 6-3 10-8 11l-1-3c3-1 4-3 4-6h-4z" fill="#8a9ab0"/>
</svg>
<p class="abs review-lead">Lorem ipsum dolor sit amet, consectetuer adipiscingwe elit sed diam nonummy nibh euismod tincidunt.</p>
<p class="abs review-body">Ut wisi enim ad minim veniam, quis nostrud exerci tationere ullamcorper suscipit lobortis nisl ut aliquip ex eawere erewrr commodo consequat. Duis autem vel eum iriure dolor inwer hendrerit in vulputate velit esse molestie consequat, velererr illum dolore euwere feugiat nulla facilisis at vero eros et Utrr wisi enim ad minim veniam, quis nostrud exerci tationewrw ullamcorper suscipit lobortis nis.</p>
<p class="abs review-name">- Mr. Dalton</p>
<div class="abs dots"><i class="on"></i><i></i><i></i><i></i></div>

<footer class="abs footer" role="img" aria-label="Photo of a city skyline at night"></footer>
<div class="abs chat">
  <svg class="abs" style="left:24px;top:14px" width="32" height="30" viewBox="0 0 32 30" fill="none" stroke="#fff" stroke-width="2"><circle cx="13" cy="12" r="10"/><path d="M11 9a2.5 2.5 0 1 1 3 2.4V14M13 17v1"/><path d="M20 20l6 6-1-7"/></svg>
  LIVE CHAT
</div>
<h3 class="footer-title" style="left:141px;top:4068px">QUICK INQUIRY</h3>
<div class="field" style="left:142px;top:4127px;width:282px">Name</div>
<div class="field" style="left:435px;top:4127px;width:282px">Phone</div>
<div class="field" style="left:142px;top:4177px;width:282px">Email Address</div>
<div class="field" style="left:435px;top:4177px;width:282px">Choose a Service</div>
<div class="field" style="left:142px;top:4225px;width:575px;height:71px">Enter Your Message Here ..</div>
<span class="abs btn btn-solid submit">SUBMIT</span>

<h3 class="footer-title" style="left:796px;top:4068px">CONTACT DETAILS</h3>
<div class="contact-row" style="top:4124px"><span class="ico"><svg width="14" height="18" viewBox="0 0 14 18"><path fill="var(--blue)" d="M7 0a7 7 0 0 1 7 7c0 5-7 11-7 11S0 12 0 7a7 7 0 0 1 7-7zm0 4a3 3 0 1 0 0 6 3 3 0 0 0 0-6z"/></svg></span><span><b>BRAMWELL EXTERIORS</b><br>Larkmoor Heights, Northfield</span></div>
<div class="contact-row" style="top:4184px"><span class="ico"><svg width="15" height="15" viewBox="0 0 24 24"><path fill="var(--blue)" d="M6.6 10.8a15 15 0 0 0 6.6 6.6l2.2-2.2c.3-.3.7-.4 1-.2 1.1.4 2.3.6 3.6.6.6 0 1 .4 1 1V20c0 .6-.4 1-1 1A17 17 0 0 1 3 4c0-.6.4-1 1-1h3.5c.6 0 1 .4 1 1 0 1.3.2 2.5.6 3.6.1.3 0 .7-.2 1z"/></svg></span><span style="padding-top:6px">780-555-0148</span></div>
<div class="contact-row" style="top:4234px"><span class="ico"><svg width="16" height="12" viewBox="0 0 24 18"><path fill="var(--blue)" d="M2 0h20a2 2 0 0 1 2 2v.5L12 10 0 2.5V2a2 2 0 0 1 2-2zm-2 5 12 7.5L24 5v11a2 2 0 0 1-2 2H2a2 2 0 0 1-2-2z"/></svg></span><span style="padding-top:6px">info@bramwellbuilders.ca</span></div>
<div class="contact-row" style="top:4284px"><span class="ico"><svg width="18" height="18" viewBox="0 0 20 20" fill="none" stroke="var(--blue)" stroke-width="2"><circle cx="10" cy="10" r="8"/><path d="M10 5v5l3 2"/></svg></span><span><b>OFFICE HOURS</b><br>Mon-Fri: 8:00-4:30<br>Sat-Sun &amp; Holidays: Closed</span></div>

<span class="footer-link active" style="left:144px">HOME</span>
<span class="footer-link" style="left:247px">ABOUT</span>
<span class="footer-link" style="left:358px">SERVICES</span>
<span class="footer-link" style="left:484px">MEET THE TEAM</span>
<span class="footer-link" style="left:652px">CONTACT</span>
<div class="abs footer-brand"><i class="brand-dot"></i><span class="brand-name" style="font-size:20px">BRAMWELL EXTERIORS</span></div>

<div class="abs copyright">Copyright © 2020 BRAMWELL EXTERIORS. All Rights Reserved.</div>

</body>
</html>
```